Veltrasync Template Refresh 2017

We want software development managers to remember that presentations using this template showcased Veltrasync technology: Our template must be distinctive to be remembered as showing Veltrasync technology: They must stand out from the 100s of other tech presentations they see, without being 'wacky', but professional whether bold or subtle. We are targeting the world's largest corporations.

[What do we do?] Veltrasync offers the world's first objective, fair measure of software developer productivity (Veltrasync Work Gauge) and code quality (Veltrasync PLU) metrics.

Our corporate colour is (hex) Red: 13, Green: 10, Blue: 74.

Target Market(s)

CIOs, CTOs and senior software development managers in large Enterprises.

Industry/Entity Type

Information Technology

Font styles to use
Sans Serif

Colors
0355a3

Requirements
Must have
• A memorable design
Nice to have
• Template for slides that will show a view of our User Interface (which shows graphs and charts); ideally a consistent theme to make it clear that this is our own UI, not general graphs and charts to illustrate the presentation. (None of the graphs and charts in the attached presentation are from our User Interface)
• A suggestion would be to make use of our "chord" shape (cut off circle in our logo). This could be white on a blue to appear as a cut-out window for the slide content.
Should not have
• A colourful / jokey / fun tone.

```html
<!DOCTYPE html>
<html lang="en">
<head>
<meta charset="utf-8">
<title>What is Coding Effort?</title>
<link rel="stylesheet" href="https://fonts.googleapis.com/css2?family=Source+Sans+3:wght@300;400;700&display=swap">
<style>
  :root {
    --brand-navy: #27225f;
    --ink: #1d1d24;
    --muted: #6b6b75;
    --paper: #ffffff;
    --rule: #e2e2e6;
  }
  * { margin: 0; padding: 0; box-sizing: border-box; }
  html, body {
    width: 1200px;
    height: 675px;
    overflow: hidden;
    background: var(--paper);
  }
  .slide {
    position: relative;
    width: 1200px;
    height: 675px;
    font-family: "Source Sans 3", "Source Sans Pro", sans-serif;
    color: var(--ink);
  }
  .section-intro {
    position: absolute;
    left: 115px;
    top: 316px;
    font-weight: 300;
    font-size: 30.5px;
    line-height: 36px;
    letter-spacing: -0.2px;
    white-space: nowrap;
  }
  .title-band {
    position: absolute;
    left: 0;
    top: 403px;
    width: 1200px;
    height: 68px;
    background: var(--brand-navy);
  }
  .section-title {
    position: absolute;
    left: 115px;
    top: 6px;
    font-weight: 700;
    font-size: 47px;
    line-height: 56px;
    color: var(--paper);
    letter-spacing: -0.3px;
    white-space: nowrap;
  }
  .footer {
    position: absolute;
    left: 0;
    top: 646px;
    width: 1200px;
    height: 29px;
    border-top: 1px solid var(--rule);
  }
  .brand-name {
    position: absolute;
    left: 66px;
    top: 4px;
    font-weight: 400;
    font-size: 18px;
    line-height: 20px;
    color: var(--brand-navy);
  }
  .copyright {
    position: absolute;
    left: 555px;
    top: 9px;
    font-size: 7.5px;
    color: var(--muted);
  }
  .slide-number {
    position: absolute;
    left: 1122px;
    top: 9px;
    font-size: 7.5px;
    color: var(--muted);
  }
</style>
</head>
<body>
  <main class="slide">
    <p class="section-intro">Putting Coding Effort into the context of other endeavours<br>to quantify the productivity of software developers.</p>
    <div class="title-band">
      <h1 class="section-title">What is Coding Effort?</h1>
    </div>
    <footer class="footer">
      <span class="brand-name">Veltrasync</span>
      <span class="copyright">Copyright Veltrasync Limited 2015 - 2017. All rights reserved</span>
      <span class="slide-number">Slide 01</span>
    </footer>
  </main>
</body>
</html>
```